Producer Needs a Movie Poster for a Dramatic Film

We need a movie poster for a new dramatic film called "Dust Over Morning".
Synopisis: A young drug addict (cocaine and alcohol), REED MORROW, has hit rock bottom after a continuous downward spiral of alcoholism and drug abuse, leaving him with nothing to live for. His ex-girlfriend left him. His best friend doesn’t want anything to do with him. Unable to rehabilitate himself after multiple attempts, he attempts suicide (Jumping off of a high-rise apartment building).
We want the poster to give the dark feel of the film. It should be serious and personable.
We want the three lead actors to be listed on the top of the poster from left to right (Gerald Pinsk, Corinne Velasq, Darek Ombuvia).
The title of the film, Dust Over Morning, should be in the center of the poster.
We want "Coming Soon" centered on the bottom of the poster.

No pictures will be provided for this poster, so be creative and make something special for us to use. We're looking for a variety of good ideas.

We're excited to see what you come up with!

Please, make sure you provide us with files we can easily use. Also, we would like a copy of the film title in a separate file for easy use as well. So, two files total (One with the poster, One with just the film title by itself).

Industry/Entity Type

Movie

Requirements
Must have
• We want the three lead actors to be listed on the top of the poster from left to right (Gerald Pinsk, Corinne Velasq, Darek Ombuvia).
• The title of the film, Dust Over Morning, should be in the center of the poster.
• We want "Coming Soon" centered on the bottom of the poster.
• Please, make sure you provide us with files we can easily use. Also, we would like a copy of the film title in a separate file for easy use as well. So, two files total (One with the poster, One with just the film title by itself).
Should not have
• Should not have a person on the poster unless they are unrecognizable and you can't see any characteristics. We can't have someone on the poster who won't be in the movie.
• Don't put each locations that won't be in the film either. It takes place in LOs Angeles. Mostly on a high-rise apartment building rooftop.

```html
<!DOCTYPE html>
<html lang="en">
<head>
<meta charset="utf-8">
<title>Dust Over Morning — Poster</title>
<link rel="stylesheet" href="https://fonts.googleapis.com/css2?family=Barlow+Condensed:wght@500&family=Barlow+Semi+Condensed:wght@500&display=swap">
<style>
  :root {
    --backdrop: #2a2826;
    --poster-bg: #1f1c21;
    --night-top: #19171b;
    --city-glow: #3a3236;
    --window-haze: rgba(150, 150, 150, 0.35);
    --title-gold: #b2a17c;
    --credit-white: #eceaf0;
  }
  * { margin: 0; padding: 0; box-sizing: border-box; }
  html, body {
    width: 899px;
    height: 1200px;
    overflow: hidden;
    background: var(--backdrop);
  }
  .poster {
    position: absolute;
    left: 135px;
    top: 145px;
    width: 630px;
    height: 910px;
    background: var(--poster-bg);
    overflow: hidden;
  }
  .cast-list {
    position: absolute;
    top: 16px;
    left: 0;
    width: 100%;
    display: flex;
    justify-content: space-between;
    padding: 0 22px;
    font-family: "Barlow Semi Condensed", sans-serif;
    font-weight: 500;
    font-size: 21px;
    letter-spacing: 2px;
    text-transform: uppercase;
    color: var(--credit-white);
  }
  .city-lights {
    position: absolute;
    left: 0;
    top: 130px;
    width: 100%;
    height: 190px;
    background:
      radial-gradient(ellipse 60% 30% at 50% 35%, rgba(210, 180, 140, 0.22), transparent 70%),
      linear-gradient(180deg, var(--night-top) 0%, var(--city-glow) 40%, var(--poster-bg) 100%);
  }
  .window-glow {
    position: absolute;
    left: 150px;
    top: 305px;
    width: 335px;
    height: 290px;
    background: linear-gradient(180deg, var(--window-haze), rgba(120, 120, 120, 0.2));
    filter: blur(10px);
    opacity: 0.7;
  }
  .film-title {
    position: absolute;
    left: 205px;
    top: 312px;
    font-family: "Barlow Condensed", sans-serif;
    font-weight: 500;
    font-size: 100px;
    line-height: 0.88;
    text-transform: uppercase;
    color: var(--title-gold);
  }
  .release-note {
    position: absolute;
    bottom: 34px;
    left: 0;
    width: 100%;
    text-align: center;
    font-family: "Barlow Condensed", sans-serif;
    font-weight: 500;
    font-size: 36px;
    text-transform: uppercase;
    color: var(--credit-white);
  }
</style>
</head>
<body>
  <main class="poster">
    <header class="cast-list">
      <span>Gerald Pinsk</span>
      <span>Corinne Velasq</span>
      <span>Darek Ombuvia</span>
    </header>
    <div class="city-lights" role="img" aria-label="Night view of Los Angeles city lights from a high-rise rooftop"></div>
    <div class="window-glow" role="img" aria-label="Blurred lit apartment window in the dark"></div>
    <h1 class="film-title">Dust<br>Over<br>Morning</h1>
    <p class="release-note">Coming Soon</p>
  </main>
</body>
</html>
```